Mendwise Partners
Project: Mendwise Partners
Mendwise Partners - Financial Services
Creative Brief
Professional
Karl Varner
Hillcrest Office Park 47 Bloem Street Kestrel Building Northbrook 2190
karl.varner@mendwisepartners-example.co.za
www.mendwisepartners-example.co.za
Try and use both the colour and black & white logos on the back.

```html
<!DOCTYPE html>
<html lang="en">
<head>
<meta charset="utf-8">
<title>Mendwise Partners – Business Card</title>
<link href="https://fonts.googleapis.com/css2?family=Montserrat:wght@400;500;600&display=swap" rel="stylesheet">
<style>
  :root {
    --page: #e9eaec;
    --card: #ffffff;
    --brand-blue: #1d8fc4;
    --deep-blue: #1f3f8f;
    --ink: #2f3237;
    --muted: #6b6f75;
    --rule-grey: #4a4d52;
  }
  * { box-sizing: border-box; margin: 0; padding: 0; }
  html, body { width: 1200px; height: 939px; overflow: hidden; }
  body {
    background: var(--page);
    font-family: "Montserrat", sans-serif;
    color: var(--ink);
    position: relative;
  }
  .card {
    position: absolute;
    top: 320px;
    width: 520px;
    height: 298px;
    background: var(--card);
    box-shadow: 0 6px 18px rgba(0,0,0,0.12);
    overflow: hidden;
  }
  .card--front { left: 50px; }
  .card--back { left: 630px; }

  .brand {
    position: absolute;
    left: 34px;
    top: 34px;
    display: flex;
    align-items: center;
    gap: 10px;
  }
  .brand__dot {
    width: 14px; height: 14px;
    background: var(--brand-blue);
  }
  .brand__name {
    font-weight: 500;
    font-size: 22px;
    color: var(--brand-blue);
    letter-spacing: 0.5px;
  }
  .address {
    position: absolute;
    left: 34px;
    top: 76px;
    font-size: 10px;
    line-height: 1.5;
    color: var(--muted);
  }
  .contact {
    position: absolute;
    right: 32px;
    top: 40px;
    text-align: right;
  }
  .contact__name {
    font-size: 17px;
    font-weight: 500;
    color: var(--deep-blue);
  }
  .contact__role {
    font-size: 12px;
    color: var(--ink);
    margin-top: 3px;
  }
  .contact__lines {
    margin-top: 22px;
    font-size: 10px;
    line-height: 1.6;
    color: var(--muted);
  }
  .contact__lines span { display: flex; justify-content: flex-end; align-items: center; gap: 6px; }
  .contact__lines svg { width: 9px; height: 9px; fill: var(--brand-blue); }

  .wave { position: absolute; left: 0; bottom: 0; width: 520px; height: 150px; }
  .website {
    position: absolute;
    right: 32px;
    bottom: 16px;
    font-size: 11px;
    color: #ffffff;
    letter-spacing: 0.3px;
  }

  .back-brand {
    position: absolute;
    inset: 0;
    display: flex;
    align-items: center;
    justify-content: center;
    gap: 12px;
  }
  .back-brand .brand__dot { width: 18px; height: 18px; }
  .back-brand .brand__name { font-size: 28px; }
</style>
</head>
<body>
  <section class="card card--front" aria-label="Business card front">
    <div class="brand">
      <span class="brand__dot"></span>
      <span class="brand__name">Mendwise Partners</span>
    </div>
    <p class="address">
      Hillcrest Office Park, 47 Bloem Street<br>
      Kestrel Building<br>
      Northbrook 2190
    </p>
    <div class="contact">
      <p class="contact__name">Karl Varner</p>
      <p class="contact__role">Consultant</p>
      <div class="contact__lines">
        <span>011 555 0142
          <svg viewBox="0 0 24 24"><path d="M6.6 10.8a15.1 15.1 0 0 0 6.6 6.6l2.2-2.2a1 1 0 0 1 1-.25 11.4 11.4 0 0 0 3.6.57 1 1 0 0 1 1 1V20a1 1 0 0 1-1 1A17 17 0 0 1 3 4a1 1 0 0 1 1-1h3.5a1 1 0 0 1 1 1 11.4 11.4 0 0 0 .57 3.6 1 1 0 0 1-.25 1z"/></svg>
        </span>
        <span>082 555 0187
          <svg viewBox="0 0 24 24"><path d="M7 2h10a2 2 0 0 1 2 2v16a2 2 0 0 1-2 2H7a2 2 0 0 1-2-2V4a2 2 0 0 1 2-2zm0 3v13h10V5z"/></svg>
        </span>
        <span>karl.varner@mendwisepartners-example.co.za</span>
      </div>
    </div>
    <svg class="wave" viewBox="0 0 520 150" preserveAspectRatio="none" aria-hidden="true">
      <defs>
        <linearGradient id="waveBlue" x1="0" y1="0" x2="1" y2="0">
          <stop offset="0" stop-color="#1d8fc4"/>
          <stop offset="0.6" stop-color="#2356a8"/>
          <stop offset="1" stop-color="#1f3f8f"/>
        </linearGradient>
      </defs>
      <path d="M0 40 C150 95 330 105 520 70 L520 82 C330 118 150 110 0 58 Z" fill="var(--rule-grey)"/>
      <path d="M0 68 C150 120 330 128 520 96 L520 150 L0 150 Z" fill="url(#waveBlue)"/>
      <path d="M0 62 C150 112 330 120 520 90 L520 96 C330 128 150 120 0 68 Z" fill="#9fd3ec"/>
    </svg>
    <p class="website">www.mendwisepartners-example.co.za</p>
  </section>

  <section class="card card--back" aria-label="Business card back">
    <div class="back-brand">
      <span class="brand__dot"></span>
      <span class="brand__name">Mendwise Partners</span>
    </div>
  </section>
</body>
</html>
```